Kestrova - Beverage Can

I would like to design a packaging for the Brand called Kestrova, flavour Orange. This is similar to Quenzi category. I would like to see one design for one flavour first with couple of options and later will be rolled out to other flavours.

The design should be made using 5 colours, preferably with vector graphics/Illustrations. Keyline for the artworks size, Logo and the existing graphic reference is attached.

The design will have 2 main logos and a text panel.

Let me know if you have any doubts, questions.

Reason: Not received any acceptable design yet.

Reason: Still not happy with options submitted.

Reason: I was too busy to go through the submissions.

```html
<!DOCTYPE html>
<html lang="en">
<head>
<meta charset="utf-8">
<title>Kestrova Orange – Can Label</title>
<link rel="stylesheet" href="https://fonts.googleapis.com/css2?family=Fredoka:wght@600;700&display=swap">
<style>
  :root {
    --page-bg: #f2f2f2;
    --label-deep: #d8621a;
    --label-mid: #f08a1c;
    --label-warm: #f7a91e;
    --label-glow: #fcd34a;
    --wave-light: rgba(255, 214, 90, 0.55);
    --wave-soft: rgba(255, 240, 170, 0.35);
    --wave-shade: rgba(190, 70, 20, 0.25);
    --palm-tone: rgba(206, 92, 22, 0.45);
    --brand-ink: #ffffff;
    --flavour-ink: #f5a50f;
    --flavour-edge: #ffffff;
  }

  * { margin: 0; padding: 0; box-sizing: border-box; }

  html, body {
    width: 1200px;
    height: 1165px;
    overflow: hidden;
    background: var(--page-bg);
  }

  .canvas {
    position: relative;
    width: 1200px;
    height: 1165px;
  }

  .can-label {
    position: absolute;
    left: 230px;
    top: 30px;
    width: 740px;
    height: 1104px;
    overflow: hidden;
    background: linear-gradient(180deg, var(--label-deep) 0%, var(--label-mid) 30%, var(--label-warm) 60%, var(--label-mid) 100%);
  }

  .label-waves {
    position: absolute;
    inset: 0;
    width: 100%;
    height: 100%;
  }

  .fruit-scene {
    position: absolute;
    left: 130px;
    top: 470px;
    width: 560px;
    height: 560px;
    border-radius: 50%;
    background: radial-gradient(circle at 50% 50%, rgba(255, 236, 140, 0.5) 0%, rgba(252, 196, 60, 0.3) 45%, rgba(240, 140, 30, 0) 70%);
  }

  .palm-scene {
    position: absolute;
    inset: 0;
    background: radial-gradient(ellipse 70% 40% at 90% 100%, var(--palm-tone) 0%, rgba(206, 92, 22, 0.2) 50%, rgba(206, 92, 22, 0) 100%);
  }

  .brand-name {
    position: absolute;
    left: 0;
    right: 0;
    top: 235px;
    text-align: center;
    font-family: "Fredoka", sans-serif;
    font-weight: 700;
    font-size: 150px;
    line-height: 1;
    color: var(--brand-ink);
    letter-spacing: 1px;
  }

  .flavour-name {
    position: absolute;
    left: 320px;
    top: 900px;
    font-family: "Fredoka", sans-serif;
    font-weight: 700;
    font-size: 74px;
    line-height: 1;
    color: var(--flavour-ink);
    letter-spacing: 2px;
    transform: rotate(-14deg);
    transform-origin: left bottom;
    text-shadow:
      3px 0 0 var(--flavour-edge), -3px 0 0 var(--flavour-edge),
      0 3px 0 var(--flavour-edge), 0 -3px 0 var(--flavour-edge),
      3px 3px 0 var(--flavour-edge), -3px -3px 0 var(--flavour-edge),
      3px -3px 0 var(--flavour-edge), -3px 3px 0 var(--flavour-edge);
  }
</style>
</head>
<body>
  <main class="canvas">
    <section class="can-label" aria-label="Kestrova Orange can label">
      <svg class="label-waves" viewBox="0 0 740 1104" preserveAspectRatio="none" aria-hidden="true">
        <path d="M0 560 C 180 470, 420 430, 740 500 L 740 1104 L 0 1104 Z" fill="var(--wave-light)"/>
        <path d="M0 680 C 220 600, 480 600, 740 660 L 740 1104 L 0 1104 Z" fill="var(--wave-soft)"/>
        <path d="M0 120 C 260 200, 520 150, 740 60 L 740 0 L 0 0 Z" fill="var(--wave-shade)"/>
      </svg>

      <div class="fruit-scene" role="img" aria-label="Faint illustration of a sliced orange glowing in the centre of the label"></div>
      <div class="palm-scene" role="img" aria-label="Silhouetted palm trees in warm orange at the lower right"></div>

      <h1 class="brand-name">Kestrova</h1>
      <p class="flavour-name">ORANGE</p>
    </section>
  </main>
</body>
</html>
```